Need new website for my business

I want to design a new Irrigation website for our business. What we are looking for is to have a residential section that describes providing for irrigation service for residential customers in homeowners Association. From startups to service to winterization in full residential installs.
A commercial section on our webpage describing. installation of commercial Irrigation systems. Service start-up of systems. To winterizations. Offering contract service plans for commercial customers.
Service for both commercial residential include making sure all zones are operating check for leaks adjust spray nozzles in rotors making sure all irrigation heads rotate, and are not stuck or damaged making sure that we have full coverage of each Irrigation zone for lawns. In all drip irrigation is Functioning in watering the plants accordingly. Adjusting control settings to make sure you have the right watering times during the hot dry months.
Have a landscape lighting tab:
Describing what landscape lighting and what it does to enhance curb, appeal, highlight architectural, features of landscape and transferring your outdoor space into inviting visual stunning areas with low-voltage landscape lighting
And a residential snow plowing for the Falmouth Maine area. In commercial snow, plowing and snow removal covering Scarborough south portland Portland Falmouth in Cumberland Maine for commercial Snow services. From plow & Salting parking lots to Snow removing, and Snow displacement.
we started a website but it needs a up lift and bring it to pop
our web site is willowbrookyards314.com
here are a few websites that we really like:
www.sprinklecoastal.com
www.dewpointwatering.com
www.verdantlawnsystems.com
Industry/Entity Type
Irrigation & Landscape Lighting
Coding
Coded - Design and coding required
Number of Pages Required
4 page

```html
<!DOCTYPE html>
<html lang="en">
<head>
<meta charset="UTF-8">
<title>Willowbrook Yards — Irrigation & Landscape Lighting</title>
<link rel="stylesheet" href="https://fonts.googleapis.com/css2?family=Cormorant+Garamond:wght@500;600;700&family=Lato:wght@400;700&display=swap">
<style>
  :root {
    --cream: #f4f5dd;
    --lime: #8cc63f;
    --lime-dark: #6fa52c;
    --forest: #1e3618;
    --forest-mid: #2f5224;
    --ink: #27331f;
    --muted: #5d6752;
    --sunset-top: #3a2a4d;
    --sunset-mid: #c8465a;
    --sunset-low: #f08a5d;
    --white: #ffffff;
    --footer-a: #1f6b3a;
    --footer-b: #1e6aa8;
  }
  * { box-sizing: border-box; margin: 0; padding: 0; }
  html, body { width: 849px; height: 1200px; overflow: hidden; }
  body { background: var(--cream); font-family: "Lato", sans-serif; color: var(--ink); }
  .page { width: 849px; height: 1200px; display: flex; flex-direction: column; }
  .btn { display: inline-block; background: var(--lime); color: var(--white); font-size: 10px; font-weight: 700; padding: 6px 18px; border-radius: 14px; letter-spacing: .5px; }

  /* hero */
  .hero { position: relative; height: 300px; flex: none; background: linear-gradient(180deg, var(--sunset-top) 0%, var(--sunset-mid) 45%, var(--sunset-low) 70%, #5a3a2a 78%, #1c2416 100%); text-align: center; color: var(--white); }
  .brand { position: absolute; top: 22px; left: 0; right: 0; display: flex; justify-content: center; align-items: center; gap: 8px; font-family: "Lato", sans-serif; font-weight: 700; font-size: 20px; color: var(--white); }
  .brand-dot { width: 12px; height: 12px; border-radius: 50%; background: var(--lime); }
  .hero h1 { position: absolute; top: 98px; left: 0; right: 0; font-family: "Cormorant Garamond", serif; font-weight: 600; font-size: 38px; line-height: 1.1; }
  .hero-actions { position: absolute; top: 198px; left: 0; right: 0; display: flex; justify-content: center; gap: 14px; }
  .hero-badge { position: absolute; bottom: -26px; left: 50%; width: 52px; height: 52px; margin-left: -26px; border-radius: 50%; background: linear-gradient(180deg, #f3e3a0, #b9d77a); }

  /* about */
  .about { height: 205px; flex: none; display: flex; align-items: center; gap: 40px; padding: 20px 120px 0; }
  .about-photo { width: 200px; height: 160px; background: linear-gradient(135deg, #4f7a2e, #a9c96a 60%, #3d5a22); transform: rotate(-3deg); box-shadow: 6px 6px 0 var(--lime); flex: none; }
  .eyebrow { font-size: 10px; font-weight: 700; color: var(--lime-dark); letter-spacing: 1px; text-transform: uppercase; }
  .about h2 { font-family: "Cormorant Garamond", serif; font-size: 24px; line-height: 1.1; margin: 6px 0 8px; }
  .about p { font-size: 10px; line-height: 1.5; color: var(--muted); margin-bottom: 12px; }

  /* services */
  .services { height: 200px; flex: none; background: linear-gradient(180deg, var(--forest-mid), var(--forest)); display: flex; align-items: center; gap: 24px; padding: 0 70px; color: var(--white); }
  .services-intro { width: 140px; flex: none; }
  .services-intro h2 { font-family: "Cormorant Garamond", serif; font-size: 26px; }
  .service-list { display: flex; gap: 16px; flex: 1; }
  .service-card { flex: 1; }
  .service-photo { height: 110px; margin-bottom: 8px; border: 3px solid var(--white); }
  .service-photo.res { background: linear-gradient(160deg, #8aa8c4, #5f8a3a); }
  .service-photo.com { background: linear-gradient(160deg, #6d7f8c, #3f6a2a); }
  .service-photo.light { background: linear-gradient(160deg, #1f2a3a, #c98a3a); }
  .service-card h3 { font-size: 11px; font-weight: 700; margin-bottom: 6px; }

  /* details */
  .details { height: 140px; flex: none; display: flex; align-items: center; justify-content: space-between; padding: 0 120px; }
  .details-text { width: 360px; }
  .details h2 { font-family: "Cormorant Garamond", serif; font-size: 24px; margin-bottom: 6px; }
  .details p { font-size: 10px; line-height: 1.5; color: var(--muted); }
  .details-art { width: 160px; height: 120px; flex: none; border-radius: 6px; background: linear-gradient(180deg, #eaeccb 0%, #b7d27a 45%, #6f9a3f 70%, #6b4a2a 100%); }

  /* promo */
  .promo { height: 60px; flex: none; background: linear-gradient(90deg, #3f6a2a, #6f9a3f, #3f6a2a); display: flex; align-items: center; justify-content: center; gap: 18px; color: var(--white); }
  .promo h2 { font-family: "Cormorant Garamond", serif; font-size: 22px; }

  /* gallery */
  .gallery { height: 195px; flex: none; text-align: center; padding-top: 12px; }
  .gallery-word { font-family: "Cormorant Garamond", serif; font-size: 64px; font-weight: 700; letter-spacing: 10px; color: #dfe2c4; line-height: 1; }
  .gallery h2 { font-family: "Cormorant Garamond", serif; font-size: 20px; margin: -18px 0 10px; position: relative; }
  .gallery-grid { display: flex; justify-content: center; gap: 10px; }
  .gallery-photo { width: 120px; height: 95px; }
  .g1 { background: linear-gradient(160deg, #9fb9cf, #4e7a2e); }
  .g2 { background: linear-gradient(160deg, #7a5a3a, #c4883a); }
  .g3 { background: linear-gradient(160deg, #4f7a2e, #2e4a1f); }
  .g4 { background: linear-gradient(160deg, #c6d0d8, #5d7f3a); }

  /* footer */
  .footer { flex: 1; background: linear-gradient(180deg, var(--footer-a), var(--footer-b)); color: var(--white); display: flex; flex-direction: column; align-items: center; justify-content: center; gap: 8px; text-align: center; }
  .footer .brand { position: static; font-size: 18px; }
  .footer p { font-size: 10px; opacity: .9; }
</style>
</head>
<body>
<div class="page">

  <header class="hero">
    <div class="brand"><span class="brand-dot"></span>Willowbrook Yards</div>
    <h1>Expert Irrigation &amp; Landscape Lighting<br>for Greater Maine</h1>
    <div class="hero-actions">
      <span class="btn">Get a Quote</span>
      <span class="btn">Our Services</span>
    </div>
    <div class="hero-badge" role="img" aria-label="Small sunflower emblem"></div>
  </header>

  <section class="about">
    <div class="about-photo" role="img" aria-label="Sprinkler watering a green lawn"></div>
    <div>
      <div class="eyebrow">About Us</div>
      <h2>Experienced Landscape &amp;<br>Property Maintenance Team</h2>
      <p>We install, start up and service irrigation systems for homes and businesses across southern Maine, keeping every zone running and every lawn fully covered through the hot, dry months.</p>
      <span class="btn">Learn More</span>
    </div>
  </section>

  <section class="services">
    <div class="services-intro">
      <h2>Our Services</h2>
    </div>
    <div class="service-list">
      <div class="service-card">
        <div class="service-photo res" role="img" aria-label="Residential lawn with sprinklers"></div>
        <h3>Residential Irrigation</h3>
        <span class="btn">View</span>
      </div>
      <div class="service-card">
        <div class="service-photo com" role="img" aria-label="Commercial property irrigation"></div>
        <h3>Commercial Irrigation</h3>
        <span class="btn">View</span>
      </div>
      <div class="service-card">
        <div class="service-photo light" role="img" aria-label="Home lit by landscape lighting at night"></div>
        <h3>Landscape Lighting</h3>
        <span class="btn">View</span>
      </div>
    </div>
  </section>

  <section class="details">
    <div class="details-text">
      <h2>We Care About the Details</h2>
      <p>From checking for leaks to adjusting nozzles, rotors and controller settings, we make sure every head turns freely and every drip line waters your plants just right.</p>
    </div>
    <div class="details-art" role="img" aria-label="Illustration of a small tree and flowers growing from a mound of soil"></div>
  </section>

  <section class="promo">
    <h2>Learn About Our Promotions</h2>
    <span class="btn">See Offers</span>
  </section>

  <section class="gallery">
    <div class="gallery-word">GALLERY</div>
    <h2>Our Photo Gallery</h2>
    <div class="gallery-grid">
      <div class="gallery-photo g1" role="img" aria-label="Lawn with irrigation running"></div>
      <div class="gallery-photo g2" role="img" aria-label="Garden bed with mulch"></div>
      <div class="gallery-photo g3" role="img" aria-label="Wooded yard with green grass"></div>
      <div class="gallery-photo g4" role="img" aria-label="Backyard lawn in daylight"></div>
    </div>
  </section>

  <footer class="footer">
    <div class="brand"><span class="brand-dot"></span>Willowbrook Yards</div>
    <p>Irrigation, Lighting &amp; Snow Services — Falmouth, Portland, Scarborough &amp; Cumberland</p>
    <p>willowbrookyards314.com</p>
  </footer>

</div>
</body>
</html>
```